Looking for something sharp classy and with an edge for an advanced civil construction business
Something that says professional
nothing too DARK

Target Market(s)

mining companies council civil contractors concrete works

Industry/Entity Type

Construction

Contact Information for Business Card

Ridgeline Civil Constructions
ridgelinecivilconstruction@mailtrove.net
Rewi Ashdown
0412758391

Font styles to use
Serif
Sans Serif

Colors
0455a3
0592cd
85cae6
000000
919191

Requirements
Must have
• On the back of the card must have
down the bottom small print email logo phone number

Should not have
• follow us on facebook
Ridgeline Civil Constructions

follow us on instagram
RIDGELINECIVILCONSTRUCTIONS

```html
<!DOCTYPE html>
<html lang="en">
<head>
<meta charset="utf-8">
<title>Ridgeline Civil Constructions – Business Card</title>
<link href="https://fonts.googleapis.com/css2?family=Exo+2:wght@400;500;600&display=swap" rel="stylesheet">
<style>
  :root {
    --deep-blue: #0455a3;
    --bright-blue: #0592cd;
    --sky-blue: #85cae6;
    --ink: #000000;
    --grey: #919191;
    --paper: #ffffff;
    --backdrop: #e9ebee;
  }
  * { box-sizing: border-box; margin: 0; padding: 0; }
  html, body {
    width: 1200px;
    height: 900px;
    overflow: hidden;
    background: var(--backdrop);
    font-family: "Exo 2", "Helvetica Neue", Arial, sans-serif;
  }
  .canvas {
    position: relative;
    width: 1200px;
    height: 900px;
  }
  .card {
    position: absolute;
    width: 525px;
    height: 300px;
    box-shadow: 0 10px 30px rgba(0, 0, 0, 0.18);
  }
  /* Front: contact side */
  .card--front {
    left: 585px;
    top: 110px;
    background: var(--paper);
    overflow: hidden;
  }
  .card--front .brand {
    position: absolute;
    left: 42px;
    top: 62px;
  }
  .card--front .contact {
    position: absolute;
    left: 42px;
    top: 160px;
  }
  .card--front .band {
    position: absolute;
    left: 0;
    right: 0;
    bottom: 0;
    height: 26px;
    background: var(--deep-blue);
  }
  .brand {
    display: flex;
    align-items: center;
    gap: 12px;
  }
  .brand__mark {
    width: 22px;
    height: 22px;
    flex: none;
  }
  .brand__name {
    font-weight: 600;
    font-size: 21px;
    letter-spacing: 0.5px;
    text-transform: uppercase;
    line-height: 1;
  }
  .card--front .brand__mark { background: var(--deep-blue); }
  .card--front .brand__name { color: var(--deep-blue); }

  .contact__name {
    font-weight: 600;
    font-size: 19px;
    text-transform: uppercase;
    letter-spacing: 0.3px;
    margin-bottom: 10px;
  }
  .contact__first { color: var(--deep-blue); }
  .contact__last { color: var(--bright-blue); }
  .contact__line {
    font-size: 13px;
    color: #444;
    line-height: 1.45;
    margin-left: 14px;
  }
  .contact__label {
    color: var(--deep-blue);
    font-size: 10px;
    font-weight: 500;
    text-transform: uppercase;
    margin-right: 3px;
  }

  /* Back: brand side */
  .card--back {
    left: 90px;
    top: 480px;
    background: linear-gradient(135deg, #0e5fb5 0%, var(--deep-blue) 100%);
    display: flex;
    align-items: center;
    justify-content: center;
  }
  .card--back .brand__mark { background: var(--paper); width: 28px; height: 28px; }
  .card--back .brand__name { color: var(--paper); font-size: 25px; }
</style>
</head>
<body>
  <main class="canvas">
    <section class="card card--front" aria-label="Business card, contact side">
      <div class="brand">
        <span class="brand__mark"></span>
        <span class="brand__name">Ridgeline Civil Constructions</span>
      </div>
      <div class="contact">
        <p class="contact__name"><span class="contact__first">Rewi</span> <span class="contact__last">Ashdown</span></p>
        <p class="contact__line"><span class="contact__label">Phone:</span>0412758391</p>
        <p class="contact__line"><span class="contact__label">Email:</span>ridgelinecivilconstruction@mailtrove.net</p>
      </div>
      <div class="band"></div>
    </section>

    <section class="card card--back" aria-label="Business card, brand side">
      <div class="brand">
        <span class="brand__mark"></span>
        <span class="brand__name">Ridgeline Civil Constructions</span>
      </div>
    </section>
  </main>
</body>
</html>
```